Brightwire Hollow Business cards

one side I would like my logo (uploaded) and the other side I want my details. I'm an electrician in sydney. The logo side I'm happy with just a white background and our logo in the middle.

Details for other side
24/7 Sydney Electrician
Marcus Pell
0431 587 219
marcus@brightwirehollow.com.au
brightwirehollow.com.au
icons for facebook, instagram, linked in

Industry/Entity Type

electrician

Contact Information for Business Card

company info

```html
<!DOCTYPE html>
<html lang="en">
<head>
<meta charset="UTF-8">
<title>Brightwire Hollow – Business Cards</title>
<link rel="stylesheet" href="https://fonts.googleapis.com/css2?family=Poppins:wght@300;400;700&family=Roboto:wght@500&display=swap">
<style>
  :root {
    --stage: #c9c9cb;
    --card-white: #f4f4f4;
    --card-black: #050505;
    --ink: #1d1d1f;
    --red: #e3181b;
    --white: #ffffff;
  }
  * { box-sizing: border-box; margin: 0; padding: 0; }
  html, body {
    width: 1200px; height: 1100px; overflow: hidden;
    background: var(--stage);
  }
  .sheet {
    width: 1200px; height: 1100px;
    display: flex; flex-direction: column; align-items: center;
    justify-content: center; gap: 36px;
  }
  .card {
    position: relative;
    width: 760px; height: 464px;
    border-radius: 4px;
    box-shadow: 0 14px 34px rgba(0,0,0,0.18);
    overflow: hidden;
  }
  /* Details side */
  .card--details { background: var(--card-white); }
  .brand-mark {
    position: absolute; top: 34px; right: 38px;
    display: flex; align-items: center; gap: 12px;
    font-family: "Poppins", sans-serif; font-weight: 700;
    font-size: 20px; color: var(--red);
  }
  .brand-mark__dot {
    width: 62px; height: 62px; border-radius: 50%;
    background: var(--red);
  }
  .person {
    position: absolute; left: 52px; top: 150px;
    font-family: "Poppins", sans-serif;
    font-size: 66px; line-height: 1; color: var(--ink);
    letter-spacing: -0.5px;
  }
  .person__first { font-weight: 700; position: relative; }
  .person__first::after {
    content: ""; position: absolute; left: 0; right: 0; bottom: -18px;
    height: 4px; background: var(--red);
  }
  .person__last { font-weight: 300; }
  .contacts {
    position: absolute; left: 52px; bottom: 40px;
    list-style: none;
    font-family: "Poppins", sans-serif; font-weight: 300;
    color: var(--ink);
  }
  .contacts__item {
    display: flex; align-items: center; gap: 18px;
    font-size: 22px; line-height: 1.45;
  }
  .contacts__item--phone { font-size: 27px; font-weight: 400; margin-bottom: 12px; }
  .contacts__icon { width: 18px; height: 18px; flex: none; }
  .socials {
    position: absolute; right: 44px; bottom: 160px;
    display: flex; gap: 20px;
  }
  .socials__dot {
    width: 30px; height: 30px; border-radius: 50%;
    background: var(--ink);
  }
  .tagline {
    position: absolute; right: 0; bottom: 96px;
    background: var(--red); color: var(--white);
    font-family: "Roboto", sans-serif; font-weight: 500;
    font-size: 22px; padding: 10px 28px 10px 30px;
    border-radius: 10px 0 0 10px;
  }
  /* Logo side */
  .card--logo {
    background: var(--card-black);
    display: flex; align-items: center; justify-content: center; gap: 24px;
  }
  .logo-lockup__dot {
    width: 44px; height: 44px; border-radius: 50%; background: var(--red);
  }
  .logo-lockup__name {
    font-family: "Poppins", sans-serif; font-weight: 700;
    font-size: 64px; letter-spacing: 4px; text-transform: uppercase;
    color: var(--white);
  }
</style>
</head>
<body>
<main class="sheet">
  <section class="card card--details" aria-label="Business card, details side">
    <div class="brand-mark">
      <span>Brightwire Hollow</span>
      <span class="brand-mark__dot"></span>
    </div>

    <h1 class="person">
      <span class="person__first">Marcus</span> <span class="person__last">Pell</span>
    </h1>

    <ul class="contacts">
      <li class="contacts__item contacts__item--phone">
        <svg class="contacts__icon" viewBox="0 0 24 24" aria-hidden="true"><path fill="#e3181b" d="M6.6 10.8a15.1 15.1 0 0 0 6.6 6.6l2.2-2.2c.3-.3.7-.4 1-.2 1.1.4 2.3.6 3.6.6.6 0 1 .4 1 1V20c0 .6-.4 1-1 1A17 17 0 0 1 3 4c0-.6.4-1 1-1h3.5c.6 0 1 .4 1 1 0 1.3.2 2.5.6 3.6.1.3 0 .7-.2 1z"/></svg>
        <span>0431 587 219</span>
      </li>
      <li class="contacts__item">
        <svg class="contacts__icon" viewBox="0 0 24 24" aria-hidden="true"><path fill="#e3181b" d="M2 5h20v14H2z"/><path d="M2 5l10 8 10-8" fill="none" stroke="#f4f4f4" stroke-width="2"/></svg>
        <span>marcus@brightwirehollow.com.au</span>
      </li>
      <li class="contacts__item">
        <svg class="contacts__icon" viewBox="0 0 24 24" aria-hidden="true"><circle cx="12" cy="12" r="10" fill="#e3181b"/><path d="M2 12h20M12 2c3 3 3 17 0 20M12 2c-3 3-3 17 0 20" fill="none" stroke="#f4f4f4" stroke-width="1.5"/></svg>
        <span>brightwirehollow.com.au</span>
      </li>
    </ul>

    <div class="socials" aria-hidden="true">
      <span class="socials__dot"></span>
      <span class="socials__dot"></span>
      <span class="socials__dot"></span>
    </div>

    <p class="tagline">24/7 Sydney Electricians</p>
  </section>

  <section class="card card--logo" aria-label="Business card, logo side">
    <span class="logo-lockup__dot"></span>
    <span class="logo-lockup__name">Brightwire Hollow</span>
  </section>
</main>
</body>
</html>
```